Business Card for Industrial Distributor

We need a business card design for an industrial distributor. We sell machine parts for the manufacturing and oil industry. We would like the cards to look clean and modern but with a touch of industry.

Our colors are blue/white.

Please feel free to visit our website www.korvanlineusa.com

Target Market(s)

mexican manufacturers in the automobile/aerospace industry

Industry/Entity Type

Industrial

Colors
ffffff
0555a3

```html
<!DOCTYPE html>
<html lang="en">
<head>
<meta charset="utf-8">
<title>Korvanline Business Card</title>
<link rel="stylesheet" href="https://fonts.googleapis.com/css2?family=Lato:wght@400;700;900&display=swap">
<style>
  :root {
    --stage: #3c3c3c;
    --blue: #0555a3;
    --blue-deep: #2a55a0;
    --blue-light: #2a6fb8;
    --navy: #23308f;
    --grey: #8c8c8c;
    --grey-line: #9a9a9a;
    --white: #ffffff;
  }
  html, body {
    margin: 0; padding: 0;
    width: 1200px; height: 810px;
    overflow: hidden;
    background: var(--stage);
  }
  .canvas {
    position: relative;
    width: 1200px; height: 810px;
    font-family: "Lato", sans-serif;
  }
  .card {
    position: absolute;
    width: 525px; height: 300px;
    overflow: hidden;
    box-shadow: 0 6px 18px rgba(0,0,0,0.35);
  }
  /* Back side */
  .card-back {
    left: 70px; top: 90px;
    background: radial-gradient(ellipse at 45% 40%, var(--blue-light) 0%, var(--blue-deep) 75%);
    color: var(--white);
  }
  .back-mark {
    position: absolute;
    left: 0; right: 0; top: 100px;
    display: flex; align-items: center; justify-content: center; gap: 12px;
  }
  .back-mark .dot {
    width: 34px; height: 34px; border-radius: 50%;
    background: var(--white);
  }
  .back-mark .brand {
    font-weight: 900; font-size: 40px; letter-spacing: 0.5px;
  }
  .back-url {
    position: absolute; left: 0; right: 0; bottom: 28px;
    text-align: center; font-size: 13px; letter-spacing: 0.3px;
  }
  /* Front side */
  .card-front {
    left: 605px; top: 420px;
    background: var(--white);
  }
  .front-brand {
    position: absolute; left: 34px; top: 46px;
    display: flex; align-items: center; gap: 12px;
    color: var(--navy);
  }
  .front-brand .dot {
    width: 42px; height: 42px; border-radius: 50%;
    background: var(--blue);
  }
  .front-brand .brand {
    font-weight: 900; font-size: 44px; letter-spacing: 0.3px;
  }
  .person {
    position: absolute; right: 40px; top: 62px;
    text-align: right;
  }
  .person .name {
    font-weight: 700; font-size: 21px; color: var(--navy);
  }
  .person .role {
    font-size: 12px; color: var(--grey); margin-top: 1px;
  }
  .edge-tab {
    position: absolute; right: 0; top: 52px;
    width: 7px; height: 28px; border-radius: 4px 0 0 4px;
    background: var(--navy);
  }
  .company {
    position: absolute; left: 48px; top: 128px;
    font-size: 12px; line-height: 16px; color: var(--grey);
  }
  .company .company-name { color: var(--navy); font-weight: 700; }
  .contacts {
    position: absolute; left: 60px; top: 180px;
    margin: 0; padding: 0; list-style: none;
    font-size: 12px; line-height: 16px; color: var(--grey);
  }
  .contacts li { display: flex; align-items: center; gap: 8px; }
  .contacts svg { width: 12px; height: 12px; fill: var(--navy); }
  .contacts .web { color: var(--navy); }
  .swoosh { position: absolute; left: 0; top: 0; }
</style>
</head>
<body>
<main class="canvas">
  <section class="card card-back" aria-label="Card back">
    <div class="back-mark">
      <span class="dot"></span>
      <span class="brand">Korvanline</span>
    </div>
    <div class="back-url">www.korvanlineusa.com</div>
  </section>

  <section class="card card-front" aria-label="Card front">
    <svg class="swoosh" width="525" height="300" viewBox="0 0 525 300">
      <path d="M0,300 L0,296 C260,292 420,220 525,110 L525,300 Z" fill="var(--blue-deep)"/>
      <path d="M0,283 C260,279 420,206 525,95" fill="none" stroke="var(--grey-line)" stroke-width="4"/>
    </svg>
    <span class="edge-tab"></span>
    <div class="front-brand">
      <span class="dot"></span>
      <span class="brand">Korvanline</span>
    </div>
    <div class="person">
      <div class="name">Daniel Reyes</div>
      <div class="role">President &amp; CEO</div>
    </div>
    <div class="company">
      <div class="company-name">korvanline international Corp.</div>
      <div>4820 Harbor Mill Rd,</div>
      <div>Laredo, TX 78041</div>
    </div>
    <ul class="contacts">
      <li><svg viewBox="0 0 12 12"><path d="M1 4 Q6 0 11 4 L9 6 L8 4.5 Q6 4 4 4.5 L3 6 Z M3 7 H9 V11 H3 Z"/></svg>(555) 210 - 4400</li>
      <li><svg viewBox="0 0 12 12"><path d="M3 1 H9 V4 H3 Z M1 5 H11 V10 H9 V8 H3 V10 H1 Z M3 9 H9 V11 H3 Z"/></svg>(555) 210 - 4413</li>
      <li><svg viewBox="0 0 12 12"><path d="M1 3 H11 V10 H1 Z M1.5 3.5 L6 7 L10.5 3.5" stroke="var(--white)" stroke-width="0.8"/></svg>sales@korvanlineusa.com</li>
      <li class="web"><svg viewBox="0 0 12 12"><circle cx="6" cy="6" r="5" fill="none" stroke="var(--navy)" stroke-width="1"/><path d="M1 6 H11 M6 1 V11 M2 3.5 H10 M2 8.5 H10" stroke="var(--navy)" stroke-width="0.7" fill="none"/></svg>www.korvanlineusa.com</li>
    </ul>
  </section>
</main>
</body>
</html>
```